Product Sales Website Design - E-commerce - Shopify etc

We have been selling printing equipment for some time now and think that it will be useful to sell the products on the internet, using a simple e-commerce platform, such as shopify etc. There are roughly a few dozen products - so basically, the idea is to have a modern, simple and clean home page. When someone looks at it, they think, this is it - I want to buy here. I am not going to impose any ideas or say how I want it done.

Just so you know, at the moment there are three categories of products. One being printers, scanners and accessories.

I am excited by this whole project and don't want to have good designers backing out because they feel i am imposing restrictions. Feel free to impress me.

Industry/Entity Type

E-Commerce

Requirements
Must have
• integration with an e-commerce platform is a must or show how to integrate, so I can easily introduce further products.

```html
<!DOCTYPE html>
<html lang="en">
<head>
<meta charset="utf-8">
<title>Inkwell – Printers, Scanners &amp; Accessories</title>
<link rel="stylesheet" href="https://fonts.googleapis.com/css2?family=Open+Sans:wght@400;600;700&display=swap">
<style>
:root{
  --page:#ebebeb;
  --green:#6cbd45;
  --green-dark:#2b7a12;
  --navy:#1f4e9c;
  --sky:#5b9be8;
  --orange:#f7a532;
  --white:#ffffff;
  --ink:#333333;
  --muted:#777777;
  --price-bar:#8e99a8;
  --line:#d8d8d8;
}
*{box-sizing:border-box;margin:0;padding:0}
html,body{width:1200px;height:882px;overflow:hidden}
body{background:var(--page);font-family:"Open Sans",Arial,sans-serif;color:var(--ink);position:relative}
.abs{position:absolute}
svg{display:block}

/* header */
.brand{left:81px;top:0;width:151px;height:135px;background:var(--green);display:flex;align-items:center;justify-content:center;gap:10px;color:var(--white);font-size:28px;font-weight:600}
.brand-square{width:14px;height:14px;background:var(--white)}
.masthead{left:232px;top:0;width:888px;height:135px;background:var(--navy)}
.utility{position:absolute;right:0;top:0;height:33px;display:flex;align-items:center;color:var(--white);font-size:12.5px}
.utility a{color:var(--white);text-decoration:none;padding:0 14px;display:flex;align-items:center;gap:14px}
.utility .sep{width:8px;height:7px;border-top:2px solid #fff;border-bottom:2px solid #fff}
.select{height:33px;background:var(--green);color:#fff;display:flex;align-items:center;justify-content:space-between;padding:0 10px;margin-left:3px;font-size:12.5px}
.select.currency{width:72px}
.select.lang{width:120px;gap:8px;justify-content:flex-start}
.flag{width:16px;height:11px;background:#fff;position:relative}
.flag::before{content:"";position:absolute;left:6px;top:0;width:4px;height:11px;background:#d22}
.flag::after{content:"";position:absolute;left:0;top:4px;width:16px;height:3px;background:#d22}
.caret{width:0;height:0;border-left:4px solid transparent;border-right:4px solid transparent;border-top:5px solid #fff;margin-left:auto}
.popular{position:absolute;left:18px;top:56px;color:#fff;font-size:12.5px;display:flex;gap:11px}
.popular strong{font-weight:700}
.popular .more{color:var(--green)}
.search{position:absolute;left:17px;top:82px;width:553px;height:44px;background:#fff;display:flex;align-items:center}
.search .cat{width:167px;padding-left:9px;color:#777;font-size:13px;border-right:1px solid var(--line);height:100%;display:flex;align-items:center}
.search .kw{padding-left:16px;color:#aaa;font-size:11.5px;flex:1}
.search .go{width:46px;height:44px;background:var(--green);display:flex;align-items:center;justify-content:center}
.icon-btn{position:absolute;top:82px;width:46px;height:44px;display:flex;align-items:center;justify-content:center}
.account{position:absolute;left:728px;top:82px;width:152px;height:44px;background:var(--sky);color:#fff;display:flex;align-items:center;gap:12px;padding-left:8px;font-size:12px;font-weight:600;line-height:1.35}

/* categories */
.panel-head{height:54px;background:var(--green);color:#fff;display:flex;align-items:center;gap:14px;padding-left:6px;font-size:16px;text-transform:uppercase}
.badge{width:38px;height:38px;border:2px solid #fff;border-radius:50%;display:flex;align-items:center;justify-content:center}
.categories{left:81px;top:163px;width:239px;height:325px;background:var(--navy)}
.cat-list{list-style:none;padding:18px 10px 0 27px}
.cat-list li{color:#fff;font-size:13px;height:28.5px;display:flex;justify-content:space-between;align-items:center}
.cat-list li.strong{font-weight:600}
.cat-list .chev{width:6px;height:6px;border-top:1.5px solid #fff;border-right:1.5px solid #fff;transform:rotate(45deg)}
.plus{position:absolute;right:0;bottom:0;width:27px;height:25px;background:var(--green);display:flex;align-items:center;justify-content:center}

/* tabs */
.tab{top:163px;height:54px;color:#fff;display:flex;align-items:center;justify-content:center;font-size:17px;border:3px solid #fff;border-width:0}
.tab.printers{left:346px;width:77px;background:var(--green)}
.tab.scanners{left:427px;width:86px;background:var(--sky)}
.tab.accessories{left:517px;width:176px;background:var(--sky)}
.contact{left:696px;top:163px;width:424px;height:54px;background:var(--green);color:#fff;display:flex;align-items:center}
.contact .phone-box{width:52px;height:54px;display:flex;align-items:center;justify-content:center;border-right:3px solid #fff;margin-right:24px}
.contact p{font-size:13px;line-height:1.55}
.contact b{font-weight:700}

/* hero */
.hero{left:346px;top:222px;width:774px;height:266px;background:var(--green-dark)}
.hero h1{position:absolute;left:19px;top:56px;color:#fff;font-size:21px;font-weight:600}
.hero p{position:absolute;left:19px;top:96px;width:340px;color:#fff;font-size:12.5px;line-height:1.6}
.hero .cta{position:absolute;left:19px;top:151px;width:127px;height:36px;background:var(--sky);color:#fff;font-size:13.5px;display:flex;align-items:center;gap:18px;padding-left:10px}
.hero .dots{position:absolute;left:19px;top:233px;display:flex;gap:8px}
.dot{width:21px;height:21px;border-radius:50%;border:2px solid #fff;background:var(--sky);color:#fff;font-size:10px;display:flex;align-items:center;justify-content:center}
.dot.on{background:var(--green)}
.hero-media{position:absolute;left:384px;top:28px;width:312px;height:216px;background:linear-gradient(160deg,#3a3a3a,#1a1a1a 60%,#6b2a8a);border-radius:6px}

/* news */
.news{left:81px;top:514px;width:239px;height:368px;background:#fff}
.news-item{display:flex;gap:12px;padding:20px 0 0 8px;height:74px}
.cal{width:34px;height:40px;border:2px solid #9a9a9a;border-top-width:7px;border-radius:3px;color:#777;font-size:11px;text-align:center;line-height:1.1;padding-top:3px;position:relative}
.news-body h3{font-size:12px;font-weight:700;color:#444}
.news-body p{font-size:10.5px;color:#777;line-height:1.45}
.news-body .row{display:flex;justify-content:space-between;width:164px}
.read{color:var(--green);font-size:9.5px;display:flex;gap:4px;align-items:center}
.read i{width:9px;height:9px;background:var(--green);display:inline-block}

/* featured */
.featured{left:346px;top:514px;width:656px;height:53px;background:var(--navy);color:#fff}
.featured .panel-head{background:none}
.arrow{top:514px;width:50px;height:53px;background:var(--sky);display:flex;align-items:center;justify-content:center}
.card{top:582px;width:239px;height:284px;background:#fff}
.card .media{position:absolute;left:22px;top:32px;width:195px;height:130px;background:linear-gradient(150deg,#4a4a4a,#1d1d1d 60%,#8a5a2a);border-radius:4px}
.tag{position:absolute;left:9px;top:9px;width:37px;height:37px;border-radius:50%;color:#fff;font-size:10px;font-weight:700;display:flex;align-items:center;justify-content:center}
.tag.sale{background:var(--orange)}
.tag.new{background:var(--green)}
.card h4{position:absolute;left:0;right:0;top:197px;text-align:center;font-weight:400;font-size:15px;color:#555}
.price-bar{position:absolute;left:0;bottom:0;width:239px;height:45px;background:var(--price-bar);display:flex;align-items:center;color:#fff;font-size:15px;font-weight:600;padding-left:14px}
.price-bar s{font-weight:400;margin-left:18px;font-size:14px}
.price-bar .cart{position:absolute;right:45px;top:0;width:45px;height:45px;background:var(--sky);display:flex;align-items:center;justify-content:center}
.price-bar .fav{position:absolute;right:0;top:0;width:45px;height:45px;background:var(--orange);display:flex;align-items:center;justify-content:center}
</style>
</head>
<body>

<header>
  <div class="abs brand"><span class="brand-square"></span>Inkwell</div>
  <div class="abs masthead">
    <nav class="utility">
      <a href="#">About us <span class="sep"></span></a>
      <a href="#">Contact us <span class="sep"></span></a>
      <a href="#">Site map</a>
      <div class="select currency">USD <span class="caret"></span></div>
      <div class="select lang"><span class="flag"></span>English <span class="caret"></span></div>
    </nav>
    <div class="popular"><strong>Popular Searches:</strong><span>corvo</span><span>catu hazi kate</span><span>clogs</span><span>kate</span><span>red</span><span class="more">More »</span></div>
    <form class="search">
      <div class="cat">Categories</div>
      <svg width="10" height="10"><polygon points="2,0 10,5 2,10" fill="#bbb"/></svg>
      <div class="kw">Enter your keyword...</div>
      <div class="go"><svg width="22" height="20" fill="none" stroke="#fff" stroke-width="2"><circle cx="8" cy="8" r="6"/><line x1="12" y1="12" x2="17" y2="18"/><line x1="15" y1="5" x2="21" y2="5"/><line x1="15" y1="9" x2="21" y2="9"/></svg></div>
    </form>
    <div class="icon-btn" style="left:623px;background:var(--orange)"><svg width="30" height="30"><circle cx="15" cy="15" r="13" fill="none" stroke="#fff" stroke-width="2"/><path d="M15 21 L9 15 A3.4 3.4 0 0 1 15 10.5 A3.4 3.4 0 0 1 21 15 Z" fill="#fff"/></svg></div>
    <div class="icon-btn" style="left:675px;background:var(--sky)"><svg width="26" height="22" fill="none" stroke="#fff" stroke-width="2"><polyline points="1,2 5,2 8,15 22,15 24,6 7,6"/><circle cx="10" cy="19" r="1.8" fill="#fff"/><circle cx="20" cy="19" r="1.8" fill="#fff"/></svg></div>
    <div class="account"><svg width="32" height="24" fill="#fff"><circle cx="10" cy="6" r="5"/><path d="M1 23 a9 9 0 0 1 18 0z"/><circle cx="23" cy="7" r="4"/><path d="M17 20 a8 8 0 0 1 14 0v3h-12z"/></svg><span>Hello. Sign in<br>My Account</span></div>
  </div>
</header>

<aside class="abs categories">
  <div class="panel-head"><span class="badge"><svg width="20" height="20"><polygon points="10,1 12.6,7.3 19.5,7.6 14.1,11.9 16,18.5 10,14.7 4,18.5 5.9,11.9 0.5,7.6 7.4,7.3" fill="#fff"/></svg></span>Categories</div>
  <ul class="cat-list">
    <li class="strong">Printers <span class="chev"></span></li>
    <li class="strong">Scanners <span class="chev"></span></li>
    <li>Phones &amp; PDAs <span class="chev"></span></li>
    <li>Components</li>
    <li>Tablets</li>
    <li>Cameras</li>
    <li>Furniture</li>
    <li>Kids Store</li>
  </ul>
  <div class="plus"><svg width="16" height="16"><rect x="6.5" y="0" width="3" height="16" fill="#fff"/><rect x="0" y="6.5" width="16" height="3" fill="#fff"/></svg></div>
</aside>

<nav>
  <div class="abs tab printers">Printers</div>
  <div class="abs tab scanners">Scanners</div>
  <div class="abs tab accessories">Accessories</div>
</nav>
<div class="abs contact">
  <div class="phone-box"><svg width="34" height="34" fill="none" stroke="#fff" stroke-width="2"><circle cx="17" cy="17" r="15"/><path d="M12 10 l3 0 l1.5 4 l-2 1.5 a9 9 0 0 0 4.5 4.5 l1.5 -2 l4 1.5 l0 3 a2 2 0 0 1 -2 2 a14 14 0 0 1 -12.5 -12.5 a2 2 0 0 1 2 -2z" fill="#fff" stroke="none"/></svg></div>
  <p><b>1-800-555-0142</b><br>Call us Monday - Saturday: 8:30 am - 6:00 pm</p>
</div>

<section class="abs hero">
  <h1>Jaten caton vate</h1>
  <p>Moren dolor sit amet, consectetur adipiscing elit. Integer condimentum hendrerit adipiscing. Duis ...</p>
  <a class="cta">View Detail <svg width="24" height="24" fill="none" stroke="#fff" stroke-width="2"><circle cx="12" cy="12" r="10.5"/><polyline points="7,12 16,12"/><polyline points="12,8 16,12 12,16"/></svg></a>
  <div class="dots"><span class="dot">1</span><span class="dot">2</span><span class="dot on">3</span></div>
  <div class="hero-media" role="img" aria-label="Photo of a black multifunction inkjet printer with a colourful printed fish photo in its tray"></div>
</section>

<aside class="abs news">
  <div class="panel-head"><span class="badge"><svg width="20" height="20"><polygon points="10,1 12.6,7.3 19.5,7.6 14.1,11.9 16,18.5 10,14.7 4,18.5 5.9,11.9 0.5,7.6 7.4,7.3" fill="#fff"/></svg></span>News</div>
  <article class="news-item"><div class="cal">23<br>oct</div><div class="news-body"><h3>Storefront theme</h3><p>Fusce euismod consequat ante.</p><div class="row"><p>Lorem dolor...</p><span class="read">Read more <i></i></span></div></div></article>
  <article class="news-item"><div class="cal">23<br>oct</div><div class="news-body"><h3>Storefront theme</h3><p>Fusce euismod consequat ante.</p><div class="row"><p>Lorem dolor...</p><span class="read">Read more <i></i></span></div></div></article>
  <article class="news-item"><div class="cal">22<br>oct</div><div class="news-body"><h3>Storefront theme</h3><p>Fusce euismod consequat ante.</p><div class="row"><p>Lorem dolor...</p><span class="read">Read more <i></i></span></div></div></article>
  <article class="news-item"><div class="cal">23<br>oct</div><div class="news-body"><h3>Storefront theme</h3><p>Fusce euismod consequat ante.</p><div class="row"><p>Lorem dolor...</p><span class="read">Read more <i></i></span></div></div></article>
</aside>

<section>
  <div class="abs featured"><div class="panel-head"><span class="badge"><svg width="20" height="20" fill="none" stroke="#fff" stroke-width="2.5"><polyline points="3,10 8,15 17,4"/></svg></span>Featured Products</div></div>
  <div class="abs arrow" style="left:1009px"><svg width="28" height="28" fill="none" stroke="#fff" stroke-width="2"><circle cx="14" cy="14" r="12"/><polyline points="16,9 11,14 16,19"/></svg></div>
  <div class="abs arrow" style="left:1065px;width:55px"><svg width="28" height="28" fill="none" stroke="#fff" stroke-width="2"><circle cx="14" cy="14" r="12"/><polyline points="12,9 17,14 12,19"/></svg></div>

  <article class="abs card" style="left:346px">
    <div class="media" role="img" aria-label="Photo of a flatbed scanner with its lid open"></div>
    <span class="tag sale">SALE</span>
    <h4>Turem miten bokan gatem</h4>
    <div class="price-bar">$70.00 <s>$78.00</s>
      <span class="cart"><svg width="26" height="22" fill="none" stroke="#fff" stroke-width="2"><polyline points="1,2 5,2 8,15 22,15 24,6 7,6"/><circle cx="10" cy="19" r="1.8" fill="#fff"/><circle cx="20" cy="19" r="1.8" fill="#fff"/></svg></span>
      <span class="fav"><svg width="28" height="28"><circle cx="14" cy="14" r="12" fill="none" stroke="#fff" stroke-width="2"/><path d="M14 20 L8.5 14.5 A3.2 3.2 0 0 1 14 10 A3.2 3.2 0 0 1 19.5 14.5 Z" fill="#fff"/></svg></span>
    </div>
  </article>
  <article class="abs card" style="left:613px">
    <div class="media" role="img" aria-label="Photo of a black multifunction inkjet printer"></div>
    <span class="tag new">NEW</span>
    <h4>Tuka mosen polas</h4>
    <div class="price-bar">$33.00
      <span class="cart"><svg width="26" height="22" fill="none" stroke="#fff" stroke-width="2"><polyline points="1,2 5,2 8,15 22,15 24,6 7,6"/><circle cx="10" cy="19" r="1.8" fill="#fff"/><circle cx="20" cy="19" r="1.8" fill="#fff"/></svg></span>
      <span class="fav"><svg width="28" height="28"><circle cx="14" cy="14" r="12" fill="none" stroke="#fff" stroke-width="2"/><path d="M14 20 L8.5 14.5 A3.2 3.2 0 0 1 14 10 A3.2 3.2 0 0 1 19.5 14.5 Z" fill="#fff"/></svg></span>
    </div>
  </article>
  <article class="abs card" style="left:880px">
    <div class="media" role="img" aria-label="Photo of a flatbed scanner with its lid open"></div>
    <h4>Quaten mose riga buson</h4>
    <div class="price-bar">$76.00
      <span class="cart"><svg width="26" height="22" fill="none" stroke="#fff" stroke-width="2"><polyline points="1,2 5,2 8,15 22,15 24,6 7,6"/><circle cx="10" cy="19" r="1.8" fill="#fff"/><circle cx="20" cy="19" r="1.8" fill="#fff"/></svg></span>
      <span class="fav"><svg width="28" height="28"><circle cx="14" cy="14" r="12" fill="none" stroke="#fff" stroke-width="2"/><path d="M14 20 L8.5 14.5 A3.2 3.2 0 0 1 14 10 A3.2 3.2 0 0 1 19.5 14.5 Z" fill="#fff"/></svg></span>
    </div>
  </article>
</section>

</body>
</html>
```